Display Ad for Local Publication

We have never advertised before but now I would like to have an ad running in our local, community magazine. Our business is Cedar Hollow Mini Storage located in Harbor Point, WA. PL is a small community (+/-2,500 people located across the Puget Sound from Seattle. The monthly magazine, The Tidings, covers all kinds of local news and activities and carries a number of ads from local businesses. Our is the only mini storage in Harbor Point. We have enclosed storage units of various sizes and outdoor parking spaces for boats, trailers and RVs. I am enclosing a business card and the size requirements for Tidings advertisements. I want to develop a 1/8 page ad.

```html
<!DOCTYPE html>
<html lang="en">
<head>
<meta charset="utf-8">
<title>Cedar Hollow Mini Storage – Display Ad</title>
<link rel="stylesheet" href="https://fonts.googleapis.com/css2?family=Bitter:wght@700&family=Lato:ital,wght@1,700&display=swap">
<style>
  :root {
    --green: #4fbb6e;
    --charcoal: #58595b;
    --white: #ffffff;
    --rule: #e3e4e5;
    --backdrop: #cbcbcb;
  }
  * { margin: 0; padding: 0; box-sizing: border-box; }
  html, body { width: 1200px; height: 829px; overflow: hidden; background: var(--backdrop); }
  .ad {
    position: absolute; left: 0; top: 42px;
    width: 1200px; height: 744px;
    background: var(--white);
  }
  .ad-header {
    position: absolute; left: 0; top: 0; width: 100%; height: 184px;
    background: var(--green);
  }
  .business-name {
    position: absolute; left: 0; top: 36px; width: 100%;
    text-align: center; color: var(--white); white-space: nowrap;
    font-family: "Bitter", Georgia, serif; font-weight: 700; font-size: 84px; line-height: 1;
  }
  .tagline {
    position: absolute; left: 157px; top: 145px; width: 888px; height: 83px;
    background: var(--charcoal); border: 3px solid var(--white);
    color: var(--white); text-align: center; white-space: nowrap;
    font-family: "Bitter", Georgia, serif; font-weight: 700; font-size: 48px; line-height: 75px;
  }
  .features { position: absolute; left: 168px; top: 231px; width: 931px; list-style: none; }
  .feature {
    height: 88px; border-bottom: 2px solid var(--rule);
    display: flex; align-items: center; gap: 14px;
    color: var(--charcoal); white-space: nowrap;
    font-family: "Lato", Arial, sans-serif; font-style: italic; font-weight: 700; font-size: 42px;
  }
  .feature-icon { width: 92px; flex: none; display: flex; justify-content: flex-end; }
  .feature-icon svg { display: block; }
  .contact-bar {
    position: absolute; left: 0; top: 603px; width: 100%; height: 67px;
    background: var(--charcoal); color: var(--white);
    display: flex; justify-content: center; align-items: center; gap: 28px;
    font-family: "Lato", Arial, sans-serif; font-style: italic; font-weight: 700; font-size: 42px;
  }
  .contact-item, .address { display: flex; align-items: center; gap: 14px; white-space: nowrap; }
  .address {
    position: absolute; left: 0; top: 670px; width: 100%; height: 74px;
    justify-content: center; color: var(--charcoal);
    font-family: "Lato", Arial, sans-serif; font-style: italic; font-weight: 700; font-size: 42px;
  }
</style>
</head>
<body>
<main class="ad">
  <header class="ad-header">
    <h1 class="business-name">Cedar Hollow Mini Storage</h1>
  </header>
  <p class="tagline">Secure, Local &amp; Convenient Storage</p>

  <ul class="features">
    <li class="feature">
      <span class="feature-icon"><svg width="48" height="48" viewBox="0 0 44 44" fill="none" stroke="var(--green)" stroke-width="3" stroke-linejoin="round"><path d="M6 12 L22 5 L38 12 L38 32 L22 40 L6 32 Z"/><path d="M6 12 L22 19 L38 12 M22 19 V40"/><path d="M14 8.5 L30 15.5 V22"/></svg></span>
      Clean enclosed units – multiple sizes
    </li>
    <li class="feature">
      <span class="feature-icon"><svg width="68" height="38" viewBox="0 0 64 36" fill="none" stroke="var(--green)" stroke-width="3" stroke-linecap="round" stroke-linejoin="round"><path d="M16 18 L24 8 H42 L54 18 Z"/><path d="M12 18 H58 L54 24 H14 Z"/><path d="M2 24 H58"/><circle cx="40" cy="29" r="4"/></svg></span>
      Outdoor parking for boats, &amp; RVs
    </li>
    <li class="feature">
      <span class="feature-icon"><svg width="44" height="46" viewBox="0 0 40 42" fill="none" stroke="var(--green)" stroke-width="3" stroke-linejoin="round"><path d="M6 10 L34 3 V39 H6 Z"/><rect x="12" y="16" width="16" height="23"/><path d="M12 22 H28 M12 28 H28 M12 34 H28"/></svg></span>
      The only mini storage facility in Harbor Point
    </li>
    <li class="feature">
      <span class="feature-icon"><svg width="40" height="50" viewBox="0 0 36 46" fill="none" stroke="var(--green)" stroke-width="3" stroke-linecap="round" stroke-linejoin="round"><path d="M9 20 V12 a9 9 0 0 1 18 0 V20"/><rect x="4" y="20" width="28" height="23" rx="5"/><circle cx="18" cy="31.5" r="6"/><path d="M15 31.5 l2 2 l4 -4"/></svg></span>
      Safe, accessible and locally owned
    </li>
  </ul>

  <section class="contact-bar">
    <span class="contact-item">
      <svg width="32" height="32" viewBox="0 0 30 30" fill="var(--green)"><path d="M7 3 L11 3 L13 10 L10 12 C11.5 16 14 18.5 18 20 L20 17 L27 19 L27 23 C27 25 25 27 23 27 C13 26 4 17 3 7 C3 5 5 3 7 3 Z"/><path d="M17 3 a10 10 0 0 1 10 10" fill="none" stroke="var(--green)" stroke-width="2.5"/><path d="M17 8 a5 5 0 0 1 5 5" fill="none" stroke="var(--green)" stroke-width="2.5"/></svg>
      360-555-0147
    </span>
    <span class="contact-item">
      <svg width="38" height="28" viewBox="0 0 36 26" fill="var(--green)"><rect x="1" y="1" width="34" height="24" rx="2"/><path d="M3 4 L18 15 L33 4 M3 23 L14 12 M33 23 L22 12" fill="none" stroke="var(--charcoal)" stroke-width="2.5"/></svg>
      chministorage@mail.com
    </span>
  </section>

  <p class="address">
    <svg width="26" height="34" viewBox="0 0 24 32" fill="var(--green)"><path d="M12 1 C5.9 1 1 5.9 1 12 C1 20 12 31 12 31 C12 31 23 20 23 12 C23 5.9 18.1 1 12 1 Z M12 16.5 a4.5 4.5 0 1 1 0 -9 a4.5 4.5 0 0 1 0 9 Z"/></svg>
    218 Alder Lane, Harbor Point, WA
  </p>
</main>
</body>
</html>
```